Consumer Credit Attorney Needs Logo for Letterhead & Business cards

I need a basic logo or letterhead design for a new law firm in Mobile, Alabama. The firm is called "Harlow T. Benning, PC." We represent people fighting large corporations in cases involving Fair Credit Reporting, Debt Collection, Mortgage Fraud, Truth in Lending, and Wrongful Foreclosures. I don't want anything with scales of justice or columns or the typical lawyer imagery. I ride a bike to court. I keep most of my office in the cloud. I'm a different type of lawyer, and I want a design that is simple, elegant, and made primarily of blue and white.
Updates

The Job is now Payment Committed.  I look forward to seeing your submissions.  Thanks1

Project Deadline Extended
Reason: I have just recently received some new designs and provided feedback on them. You all deserve some time to consider the feedback. Thanks!

Industry/Entity Type

Business

Requirements
Nice to have
• Clear lines and a small footprint on the letterhead. I like several antique styles- Gilded Age, Rococo, Edwardian, even Art Deco.
Should not have
• The only thing I hate is 1990s clip-art style graphics. No illustrations of money, courthouses, scales, columns, etc. I also hate silly fonts, overly fancy or "handwritten" fonts, and Arial font.

```html
<!DOCTYPE html>
<html lang="en">
<head>
<meta charset="utf-8">
<title>Harlow T. Benning, PC — Letterhead</title>
<link href="https://fonts.googleapis.com/css2?family=Exo:wght@300&family=Open+Sans:wght@400&display=swap" rel="stylesheet">
<style>
  :root {
    --backdrop: #2b2b2b;
    --paper: #ffffff;
    --navy: #1b3a66;
    --rule: #dcdcdc;
    --edge-band: #e3e3e3;
    --footer-text: #6b6b6b;
  }
  html, body {
    margin: 0;
    padding: 0;
    width: 1200px;
    height: 869px;
    overflow: hidden;
    background: var(--backdrop);
  }
  .letterhead {
    position: absolute;
    left: 280px;
    top: 20px;
    width: 640px;
    height: 828px;
    background: var(--paper);
    overflow: hidden;
  }
  .letterhead__edge {
    position: absolute;
    top: 0;
    right: 0;
    width: 12px;
    height: 100%;
    background: var(--edge-band);
  }
  .letterhead__rule {
    position: absolute;
    left: 0;
    top: 93px;
    width: 398px;
    height: 1px;
    background: var(--rule);
  }
  .brand__mark {
    position: absolute;
    left: 485px;
    top: 27px;
    width: 44px;
    height: 44px;
    background: var(--navy);
  }
  .brand__name {
    position: absolute;
    right: 46px;
    top: 84px;
    margin: 0;
    font-family: "Exo", sans-serif;
    font-weight: 300;
    font-size: 14.5px;
    line-height: 18px;
    letter-spacing: 0;
    text-transform: uppercase;
    color: var(--navy);
    white-space: nowrap;
  }
  .letterhead__footer {
    position: absolute;
    left: 39px;
    top: 733px;
    margin: 0;
    font-family: "Open Sans", sans-serif;
    font-style: normal;
    font-size: 8.5px;
    line-height: 12.2px;
    color: var(--footer-text);
  }
</style>
</head>
<body>
  <main class="letterhead">
    <div class="brand__mark" aria-hidden="true"></div>
    <h1 class="brand__name">Harlow T. Benning, PC.</h1>
    <div class="letterhead__rule"></div>
    <address class="letterhead__footer">
      Proin gravida nibh vel velit<br>
      auctor aliq uet. Aenean<br>
      sollicitudi&nbsp; sollicitudin n<br>
      555-2718-093
    </address>
    <div class="letterhead__edge"></div>
  </main>
</body>
</html>
```